Business Card Design

We are looking for a business card designed for our landscaping company. We do landscaping installation & Maintenance Services. We would like to see designs that have basic landscaping in background. We also think it is important to have both of our names and phone numbers on the card. We need something that stands out a little whether it is shape of the card or thickness or design.

Industry/Entity Type

Business

Contact Information for Business Card

Pale Ridge Yardworks, paleridgeyardworks@mailbrook.net, Dale Purvine 555-213-7690, Martin Kolbey 555-864-1037

```html
<!DOCTYPE html>
<html lang="en">
<head>
<meta charset="utf-8">
<title>Pale Ridge Yardworks – Business Card</title>
<link href="https://fonts.googleapis.com/css2?family=Arimo:wght@400;700&display=swap" rel="stylesheet">
<style>
  :root {
    --card-black: #000000;
    --leaf-green: #8ee000;
    --paper-white: #ffffff;
  }
  html, body {
    margin: 0;
    padding: 0;
    width: 1200px;
    height: 700px;
    overflow: hidden;
    background: var(--card-black);
  }
  .business-card {
    position: relative;
    width: 1200px;
    height: 700px;
    background: var(--card-black);
    font-family: "Arimo", Arial, sans-serif;
    color: var(--paper-white);
  }
  .company-name {
    position: absolute;
    left: 54px;
    top: 263px;
    margin: 0;
    font-size: 62px;
    font-weight: 700;
    line-height: 68px;
    letter-spacing: 0.5px;
    text-transform: uppercase;
  }
  .company-name .line { display: block; }
  .accent { color: var(--leaf-green); }
  .email {
    position: absolute;
    left: 54px;
    top: 541px;
    margin: 0;
    font-size: 29px;
    font-weight: 400;
    line-height: 1;
  }
  .contacts {
    position: absolute;
    left: 54px;
    top: 583px;
    margin: 0;
    padding: 0;
    list-style: none;
    font-size: 28px;
    line-height: 38px;
  }
  .contact-name {
    color: var(--leaf-green);
    font-weight: 700;
  }
  .contact-phone { font-weight: 400; }
</style>
</head>
<body>
  <main class="business-card">
    <h1 class="company-name">
      <span class="line">Pale Ridge</span>
      <span class="line"><span class="accent">Yard</span>works</span>
    </h1>
    <p class="email">paleridgeyardworks@mailbrook.net</p>
    <ul class="contacts">
      <li><span class="contact-name">Dale Purvine</span> <span class="contact-phone">555-213-7690</span></li>
      <li><span class="contact-name">Martin Kolbey</span> <span class="contact-phone">555-864-1037</span></li>
    </ul>
  </main>
</body>
</html>
```